Super elegant, crisp & clean Business card design required

We recently upgraded our branding - which is on our website - tavorelstudio.com

I would like a simple, yet elegant, clean business card design please.

The font of my logo is Cinzel - and because of the natural colour - it's best to have this on a black background.

I would like to have the back of the business card - with simply my logo.

PLEASE DO NOT SUBMIT A COMPLICATED / UNCLEAN DESIGN

Industry/Entity Type

Business

Contact Information for Business Card

Dalvik Ostrander Photography

Font styles to use
Other font styles liked:
• Cinzel

Requirements
Must have
• A backpage with nothing but my logo
• Simple design - stands out
Should not have
• Colour that dont align with my logo
• Over complicated '/ non symmetrical design

```html
<!DOCTYPE html>
<html lang="en">
<head>
<meta charset="utf-8">
<title>Dalvik Ostrander Photography – Business Card</title>
<link href="https://fonts.googleapis.com/css2?family=Cinzel:wght@400&family=Open+Sans:wght@400;700&display=swap" rel="stylesheet">
<style>
  :root {
    --backdrop: #dcdcdc;
    --card-black: #000000;
    --card-white: #ffffff;
    --gold: #8b7b62;
    --gold-soft: #968468;
    --edge: #7d705c;
  }
  * { margin: 0; padding: 0; box-sizing: border-box; }
  html, body {
    width: 1200px; height: 900px; overflow: hidden;
    background: var(--backdrop);
  }
  .canvas { position: relative; width: 1200px; height: 900px; }
  .card {
    position: absolute; top: 89px; width: 420px; height: 733px;
    text-align: center; color: var(--gold);
  }
  .card--back { left: 125px; background: var(--card-black); }
  .card--front { left: 625px; background: var(--card-white); border: 2px solid var(--edge); }

  .brand-square {
    position: absolute; left: 50%; transform: translateX(-50%);
    border: 4px solid var(--gold);
  }
  .card--back .brand-square { top: 202px; width: 198px; height: 246px; }
  .card--front .brand-square { top: 84px; width: 86px; height: 104px; border-width: 3px; }

  .brand-name, .brand-line {
    position: absolute; left: 0; right: 0;
    font-family: "Cinzel", serif; font-weight: 400; color: var(--gold);
    white-space: nowrap;
  }
  .card--back .brand-name { top: 480px; font-size: 30px; }
  .card--back .brand-line { top: 516px; font-size: 13px; letter-spacing: 0.48em; padding-left: 0.48em; }
  .card--front .brand-name { top: 212px; font-size: 19px; }
  .card--front .brand-line { top: 236px; font-size: 9px; letter-spacing: 0.5em; padding-left: 0.5em; }

  .contact { position: absolute; left: 0; right: 0; top: 420px; font-family: "Open Sans", sans-serif; color: var(--gold-soft); }
  .contact__name { font-size: 30px; font-weight: 700; color: var(--gold); letter-spacing: 0.02em; line-height: 1.1; }
  .contact__role { font-size: 20px; margin-top: 4px; }
  .contact__phone { font-size: 25px; margin-top: 40px; }
  .contact__email { font-size: 19px; margin-top: 6px; }
  .contact__web { font-size: 16px; margin-top: 14px; letter-spacing: 0.02em; }
</style>
</head>
<body>
<main class="canvas">
  <section class="card card--back" aria-label="Card back">
    <div class="brand-square"></div>
    <p class="brand-name">Dalvik Ostrander</p>
    <p class="brand-line">PHOTOGRAPHY</p>
  </section>

  <section class="card card--front" aria-label="Card front">
    <div class="brand-square"></div>
    <p class="brand-name">Dalvik Ostrander</p>
    <p class="brand-line">PHOTOGRAPHY</p>

    <div class="contact">
      <p class="contact__name">ELIAS MORVEN</p>
      <p class="contact__role">Photographer</p>
      <p class="contact__phone">123 456 789</p>
      <p class="contact__email">lorem@ipsum.com</p>
      <p class="contact__web">TAVORELSTUDIO.COM</p>
    </div>
  </section>
</main>
</body>
</html>
```